Restaurant needs a vertical banner for fried catfish

Our restaurant is looking for an eye-catching 78.75in. x 36in. vertical physical banner ad for our fried catfish. Photos for the fried catfish will be provided as a reference but we will also accept anything similar to the photo. We will be using the following as our receptacle: https://www.plankoria.example/banner-stand/retractable-banner-stands/
The design must incorporate the following flavor texts:
Fried Catfish
Always Fresh!
Made from Scratch
Hand-cut Fillets
The Best Catfish in Texas
Served with fries, hush puppies, and a 32oz fountain drink
Also available by the pound!
The final design should be creative, professional, and eye-catching for customers.
Updates
Colors
Designer to choose colors to be used in the design.
Requirements
Must have
- We are open to any and all design elements, albeit the 'flavor texts' should not overpower, but complement the fried catfish photo. 'Fried Catfish' can be used in lieu of a main title/logo.
Nice to have
- Transparent or textured backgrounds that can encompass any or all part of the banner such as a cutting board, shadows, abstract, etc to show depth are a plus.
- Use of vectors or objects such as ribbons or shapes to encapsulate the 'flavor texts' are also encouraged.

```html
<!DOCTYPE html>
<html lang="en">
<head>
<meta charset="utf-8">
<title>Fried Catfish Banner</title>
<link rel="stylesheet" href="https://fonts.googleapis.com/css2?family=Crimson+Text:wght@400&family=Jost:wght@500&family=Arimo:wght@400&display=swap">
<style>
  :root {
    --olive: #87801a;
    --olive-deep: #4b4a14;
    --olive-dark: #3d3b1f;
    --rust: #93520f;
    --mustard: #c8bb1e;
    --wood-light: #b8622f;
    --wood-mid: #9c4d25;
    --wood-dark: #86401f;
    --rope: #7a5a3a;
    --white: #ffffff;
    --ink: #222222;
  }
  html, body { margin: 0; padding: 0; overflow: hidden; }
  body { width: 1200px; height: 2626px; background: var(--white); position: relative; }
  .banner { position: relative; width: 1200px; height: 2626px; overflow: hidden; background: var(--white); }
  .band { position: absolute; left: 0; width: 1200px; }
  .band--top { top: 0; height: 36px; background: var(--olive); }
  .band--bottom { top: 2580px; height: 46px; background: var(--olive); }
  .title-bar {
    top: 118px; height: 98px; background: var(--rust);
    display: flex; align-items: center; justify-content: center;
  }
  .title {
    margin: 0; color: var(--white);
    font-family: "Crimson Text", serif; font-weight: 400; font-size: 82px; letter-spacing: 1px; line-height: 1;
  }
  .band--photo-cap { top: 244px; height: 28px; background: var(--olive-deep); }
  .dish-photo {
    position: absolute; left: 0; top: 272px; width: 1200px; height: 676px;
    background: radial-gradient(ellipse at 50% 55%, #d59a45 0%, #b9793a 35%, #8b6a48 70%, #6e5a44 100%);
  }
  .fresh-tag {
    position: absolute; left: 600px; top: 802px; width: 600px; height: 92px; background: var(--white);
    display: flex; align-items: center; justify-content: flex-end; padding-right: 78px; box-sizing: border-box;
    font-family: "Arimo", sans-serif; font-size: 58px; color: var(--ink);
  }
  .column { position: absolute; left: 0; width: 264px; background: linear-gradient(90deg, #8a8518, #a29c1e); }
  .wood {
    position: absolute; left: 264px; width: 936px;
    background: linear-gradient(90deg, var(--wood-dark) 0%, var(--wood-mid) 30%, var(--wood-light) 60%, var(--wood-mid) 85%, var(--wood-dark) 100%);
  }
  .band--section-cap { top: 1030px; height: 20px; background: var(--olive-dark); }
  .promise {
    position: absolute; left: 0; top: 1118px; width: 1200px; height: 290px; background: var(--olive-dark);
    display: flex; flex-direction: column; justify-content: center; align-items: center;
    font-family: "Jost", sans-serif; font-weight: 500; color: var(--white); font-size: 68px; line-height: 88px; letter-spacing: 3px;
  }
  .promise p { margin: 0; }
  .sides {
    position: absolute; left: 0; top: 1493px; width: 1200px; height: 259px; background: var(--mustard);
    display: flex; flex-direction: column; justify-content: center; padding-left: 24px; box-sizing: border-box;
    font-family: "Jost", sans-serif; font-weight: 500; color: var(--olive-dark); font-size: 62px; line-height: 80px; letter-spacing: 2px;
  }
  .sides p { margin: 0; }
  .sides-shadow { position: absolute; left: 0; top: 1752px; width: 1042px; height: 14px; background: #8d6a55; }
  .sides-ledge { position: absolute; left: 0; top: 1766px; width: 480px; height: 18px; background: var(--olive-dark); }
  .rope-swatch { position: absolute; left: 66px; top: 1908px; width: 198px; height: 170px; background: var(--rope); }
  .base-bar { position: absolute; left: 14px; top: 2078px; width: 1186px; height: 58px; background: var(--olive-dark); }
  .by-pound {
    position: absolute; left: 0; top: 2136px; width: 1200px; height: 444px;
    display: flex; align-items: center; justify-content: center; margin: 0;
    font-family: "Crimson Text", serif; font-weight: 400; font-size: 90px; line-height: 1; color: var(--rust);
  }
</style>
</head>
<body>
<main class="banner">
  <div class="band band--top"></div>
  <header class="band title-bar"><h1 class="title">Fried Catfish</h1></header>
  <div class="band band--photo-cap"></div>
  <div class="dish-photo" role="img" aria-label="Plate of cornmeal-fried catfish fillets with fries, hush puppies and tartar sauce, tomatoes and lemons behind"></div>
  <div class="fresh-tag">Always Fresh!</div>

  <div class="column" style="top:948px;height:22px;"></div>
  <div class="wood" role="img" aria-label="Wood grain texture" style="top:948px;height:22px;"></div>

  <div class="band band--section-cap"></div>
  <div class="column" style="top:1050px;height:1028px;"></div>
  <div class="wood" role="img" aria-label="Wood grain cutting board texture" style="top:1050px;height:1028px;"></div>

  <section class="promise">
    <p>Made from Scratch</p>
    <p>Hand-cut Fillets</p>
    <p>The Best Catfish in Texas</p>
  </section>

  <section class="sides">
    <p>Served with fries, hush puppies,</p>
    <p>and a 32oz fountain drink</p>
  </section>
  <div class="sides-shadow"></div>
  <div class="sides-ledge"></div>

  <div class="rope-swatch" role="img" aria-label="Woven rope texture"></div>
  <div class="base-bar"></div>

  <p class="by-pound">Also available by the pound!</p>

  <div class="band band--bottom"></div>
</main>
</body>
</html>
```